Business Card Design - Brightpath Lending Group, Inc.

Name Tyrell Ashcombe Title Mortgage Originator
Location (800) 417-6094 x21 Since 2021
Direct (240) 731-5506 Email tashcombe@brightpathhomeloans.example
NMLS 3047718 Licensed MD
www.brightpathhomeloans.example
Name Marjorie Lynn Cotter Title Mortgage Originator
Location (800) 417-6094 x22 Since 2021
Direct (443) 619-4472 Email mcotter@brightpathhomeloans.example
NMLS 3046193 Licensed MD
www.brightpathhomeloans.example
Name Marcus Dwayne Pettigrew Title Mortgage Originator
Location (800) 417-6094 x54 Since 2021
Direct (240) 357-1264 Email mpettigrew@brightpathhomeloans.example
NMLS 3089507 Licensed MD
www.brightpathhomeloans.example
Name Neil Hartsell Title Mortgage Originator
Location (800) 417-6094 x20 Since 2021
Direct (240) 546-7029 Email nhartsell@brightpathhomeloans.example
NMLS 4038816 Licensed MD,VA
www.brightpathhomeloans.example
Name Owen Tisdale Title Mortgage Originator
Location (800) 417-6094 x23 Since 2021
Direct (240) 546-7029 Email otisdale@brightpathhomeloans.example
NMLS 3046952 Licensed MD
www.brightpathhomeloans.example
Contact Information for Business Card
Name Tyrell Ashcombe Title Mortgage Originator Location (800) 417-6094 x21 Since 2021 Direct (240) 731-5506 Email tashcombe@brightpathhomeloans.example NMLS 3047718 Licensed MD www.brightpathhomeloans.example Name Marjorie Lynn Cotter Title Mortgage Originator Location (800) 417-6094 x22 Since 2021 Direct (443) 619-4472 Email mcotter@brightpathhomeloans.example NMLS 3046193 Licensed MD www.brightpathhomeloans.example Name Marcus Dwayne Pettigrew Title Mortgage Originator Location (800) 417-6094 x54 Since 2021 Direct (240) 357-1264 Email mpettigrew@brightpathhomeloans.example NMLS 3089507 Licensed MD www.brightpathhomeloans.example Name Neil Hartsell Title Mortgage Originator Location (800) 417-6094 x20 Since 2021 Direct (240) 546-7029 Email nhartsell@brightpathhomeloans.example NMLS 4038816 Licensed MD,VA www.brightpathhomeloans.example Name Owen Tisdale Title Mortgage Originator Location (800) 417-6094 x23 Since 2021 Direct (240) 546-7029 Email otisdale@brightpathhomeloans.example NMLS 3046952 Licensed MD www.brightpathhomeloans.example
Look and feel
Each slider illustrates characteristics of the customer's brand and the style your logo design should communicate.

```html
<!DOCTYPE html>
<html lang="en">
<head>
<meta charset="utf-8">
<title>Brightpath Lending Group – Business Card</title>
<link href="https://fonts.googleapis.com/css2?family=Fira+Sans:wght@400;500;600;700&display=swap" rel="stylesheet">
<style>
  :root{
    --brand-blue:#1f63a6;
    --band-blue:#1d5d9b;
    --gold:#b3a75a;
    --gold-text:#e2c24a;
    --ink:#2b2b2b;
    --paper:#ffffff;
    --stage:#e9e6e0;
    --back-blue:#4f6fae;
  }
  *{box-sizing:border-box;margin:0;padding:0}
  html,body{width:1200px;height:1023px;overflow:hidden}
  body{background:var(--stage);font-family:"Fira Sans",sans-serif;position:relative}

  .card{position:absolute;left:220px;width:760px;height:434px;border-radius:22px;overflow:hidden;
        box-shadow:0 6px 18px rgba(0,0,0,.18)}
  .card--front{top:60px;background:var(--paper)}
  .card--back{top:530px;background:linear-gradient(160deg,#5a7dbd 0%,var(--back-blue) 55%,#4565a3 100%)}

  /* front */
  .brand{position:absolute;left:38px;top:52px;display:flex;align-items:center;gap:12px;width:270px}
  .brand__dot{width:46px;height:46px;border-radius:50%;background:var(--gold);flex:none}
  .brand__name{color:var(--brand-blue);font-weight:600;font-size:19px;line-height:1.2}

  .identity{position:absolute;left:330px;top:34px;color:var(--ink)}
  .identity__name{color:var(--brand-blue);font-weight:700;font-size:31px;line-height:1.1}
  .identity__title,.identity__nmls{font-size:17px;line-height:1.3}

  .portrait{position:absolute;right:0;top:128px;width:300px;height:232px;
            background:linear-gradient(180deg,#f3f4f7 0%,#c9d2e3 45%,#34508c 100%)}

  .contacts{position:absolute;left:40px;top:196px;list-style:none;color:var(--ink);font-size:17px}
  .contacts li{display:flex;align-items:center;gap:12px;height:29px}
  .contacts svg{width:18px;height:18px;flex:none;fill:var(--brand-blue)}

  .band{position:absolute;left:0;bottom:0;width:760px;height:78px}
  .band__address{position:absolute;left:128px;bottom:0;height:62px;display:flex;align-items:center;
                 color:#fff;font-size:22px;font-weight:500;letter-spacing:.3px;text-transform:uppercase}

  /* back */
  .family{position:absolute;right:0;top:0;width:420px;height:434px;
          background:linear-gradient(200deg,rgba(210,200,200,.55) 0%,rgba(150,150,180,.45) 50%,rgba(79,111,174,0) 100%)}
  .programs{position:absolute;left:40px;top:26px;color:#fff}
  .programs h2{color:var(--gold-text);font-size:21px;font-weight:600;margin-top:8px;line-height:1.35}
  .programs ul{list-style:none}
  .programs li{display:flex;align-items:center;gap:10px;font-size:17px;line-height:1.4}
  .programs svg{width:17px;height:17px;flex:none}
</style>
</head>
<body>

<section class="card card--front" aria-label="Card front">
  <div class="brand">
    <span class="brand__dot"></span>
    <span class="brand__name">Brightpath Lending Group, Inc.</span>
  </div>

  <div class="identity">
    <div class="identity__name">Tyrell Ashcombe</div>
    <div class="identity__title">Mortgage Originator</div>
    <div class="identity__nmls">NMLS 3047718</div>
  </div>

  <div class="portrait" role="img" aria-label="Portrait of the loan originator in a blue suit and red tie"></div>

  <ul class="contacts">
    <li><svg viewBox="0 0 24 24"><path d="M7 2h10a2 2 0 0 1 2 2v16a2 2 0 0 1-2 2H7a2 2 0 0 1-2-2V4a2 2 0 0 1 2-2zm0 3v12h10V5zm5 13.5a1 1 0 1 0 0 2 1 1 0 0 0 0-2z"/></svg>(240) 731-5506</li>
    <li><svg viewBox="0 0 24 24"><path d="M6.6 10.8a15 15 0 0 0 6.6 6.6l2.2-2.2a1 1 0 0 1 1-.25 11.4 11.4 0 0 0 3.6.57 1 1 0 0 1 1 1V20a1 1 0 0 1-1 1A17 17 0 0 1 3 4a1 1 0 0 1 1-1h3.5a1 1 0 0 1 1 1c0 1.25.2 2.45.57 3.57a1 1 0 0 1-.25 1z"/></svg>(800) 417-6094 x21</li>
    <li><svg viewBox="0 0 24 24"><path d="M7 3h8l3 3v4H7zM4 11h16a2 2 0 0 1 2 2v6a2 2 0 0 1-2 2H4a2 2 0 0 1-2-2v-6a2 2 0 0 1 2-2zm3 4v2h10v-2z"/></svg>(240) 812-4470</li>
    <li><svg viewBox="0 0 24 24"><path d="M3 5h18a1 1 0 0 1 1 1v12a1 1 0 0 1-1 1H3a1 1 0 0 1-1-1V6a1 1 0 0 1 1-1zm1 2.5V17h16V7.5l-8 5.5z"/></svg>tashcombe@brightpathhomeloans.example</li>
    <li><svg viewBox="0 0 24 24"><path d="M12 2a10 10 0 1 0 0 20 10 10 0 0 0 0-20zm6.9 9h-3a15 15 0 0 0-1.3-5.6A8 8 0 0 1 18.9 11zM12 4.1c.9 1.3 1.7 3.7 1.9 6.9h-3.8c.2-3.2 1-5.6 1.9-6.9zM9.4 5.4A15 15 0 0 0 8.1 11h-3a8 8 0 0 1 4.3-5.6zM5.1 13h3a15 15 0 0 0 1.3 5.6A8 8 0 0 1 5.1 13zm6.9 6.9c-.9-1.3-1.7-3.7-1.9-6.9h3.8c-.2 3.2-1 5.6-1.9 6.9zm2.6-1.3a15 15 0 0 0 1.3-5.6h3a8 8 0 0 1-4.3 5.6z"/></svg>www.brightpathhomeloans.example</li>
  </ul>

  <svg class="band" viewBox="0 0 760 78" preserveAspectRatio="none" aria-hidden="true">
    <polygon points="0,40 330,0 330,78 0,78" fill="var(--gold)"/>
    <polygon points="120,16 760,16 760,78 106,78" fill="var(--band-blue)"/>
  </svg>
  <div class="band__address">4200 Larkwood Road Fairhaven, MD 21047 (Since 2021)</div>
</section>

<section class="card card--back" aria-label="Card back">
  <div class="family" role="img" aria-label="Smiling family of four posed together"></div>

  <div class="programs">
    <h2>Traditional Loan Programs</h2>
    <ul>
      <li><svg viewBox="0 0 24 24"><path d="M3 13l6 6L21 5" fill="none" stroke="var(--gold-text)" stroke-width="3.5"/></svg>FHA loans starting at 580 score</li>
      <li><svg viewBox="0 0 24 24"><path d="M3 13l6 6L21 5" fill="none" stroke="var(--gold-text)" stroke-width="3.5"/></svg>FHA 203k starting at 600 score</li>
      <li><svg viewBox="0 0 24 24"><path d="M3 13l6 6L21 5" fill="none" stroke="var(--gold-text)" stroke-width="3.5"/></svg>VA starting at 600 score (100% LTV)</li>
      <li><svg viewBox="0 0 24 24"><path d="M3 13l6 6L21 5" fill="none" stroke="var(--gold-text)" stroke-width="3.5"/></svg>All Conventional loan programs.</li>
    </ul>
    <h2>Low Credit Score Programs</h2>
    <ul>
      <li><svg viewBox="0 0 24 24"><path d="M3 13l6 6L21 5" fill="none" stroke="var(--gold-text)" stroke-width="3.5"/></svg>500 score up to 70% LTV</li>
      <li><svg viewBox="0 0 24 24"><path d="M3 13l6 6L21 5" fill="none" stroke="var(--gold-text)" stroke-width="3.5"/></svg>540 score up to 75% LTV</li>
      <li><svg viewBox="0 0 24 24"><path d="M3 13l6 6L21 5" fill="none" stroke="var(--gold-text)" stroke-width="3.5"/></svg>580 score up to 96.5% LTV</li>
    </ul>
    <h2>Alternative Loan Programs</h2>
    <ul>
      <li><svg viewBox="0 0 24 24"><path d="M3 13l6 6L21 5" fill="none" stroke="var(--gold-text)" stroke-width="3.5"/></svg>Investor Fix &amp; Flip Rehab Loans</li>
      <li><svg viewBox="0 0 24 24"><path d="M3 13l6 6L21 5" fill="none" stroke="var(--gold-text)" stroke-width="3.5"/></svg>Investor Stated Loans</li>
      <li><svg viewBox="0 0 24 24"><path d="M3 13l6 6L21 5" fill="none" stroke="var(--gold-text)" stroke-width="3.5"/></svg>Foreign National Loans</li>
      <li><svg viewBox="0 0 24 24"><path d="M3 13l6 6L21 5" fill="none" stroke="var(--gold-text)" stroke-width="3.5"/></svg>Limited Documentation Loans (1 year tax or W2)</li>
    </ul>
  </div>
</section>

</body>
</html>
```